Web Design Project

We are looking for a beautiful, clean web page design for our new web service: Tavernik. The idea behind tavernik is simple. People tell us where they live and what they love, and we point them towards interesting offers, places and events near them - as reviewed by our experts and their friends. It is available on the web and by phone. We have chosen our logo and know the elements we want on each page. Now we just need a whole a great design to pull it all together.
///
TaVernik
locate, explore and discover the best of your city with tavernik
Discover your cities hottest offers
places & venues while sharing
the things that mean the most to you.
Join for free today!
//
Note: we have also had some feedback that the name is difficult to read/pronounce, so we might want to change the color of the word be in tavernik so that it stands out. suggestions welcome.
Target Market(s)
Young, urban, savvy consumers
We are looking at this site for inspiration
https://strovento.example/
elements: blog:latest news, top picks // members area // categories: fashion & beauty; food & drink; entertainment & events

```html
<!DOCTYPE html>
<html lang="en">
<head>
<meta charset="utf-8">
<title>Tavernik</title>
<link rel="stylesheet" href="https://fonts.googleapis.com/css2?family=Marck+Script&family=Delius&family=Fredoka:wght@600&family=Arimo:wght@400&display=swap">
<style>
  :root{
    --brand-blue:#2a86c4;
    --bar-blue:#0a6cb7;
    --join-yellow:#f5ad00;
    --ink:#3d3d3d;
    --muted:#555;
    --paper:#ffffff;
    --mist:#f1f1f1;
    --header-top:#f7f7f7;
    --header-bottom:#e9e9e9;
  }
  *{box-sizing:border-box;margin:0;padding:0}
  a{text-decoration:none}
  html,body{width:1200px;height:1003px;overflow:hidden;background:var(--mist)}
  .page{position:relative;width:1200px;height:1003px;overflow:hidden;
    background:linear-gradient(180deg,#f4f4f4 0%,#ececec 100%);font-family:"Arimo",Arial,sans-serif}

  .site-header{position:absolute;left:0;top:0;width:1200px;height:232px;
    background:radial-gradient(ellipse at 50% 30%,#ffffff 0%,var(--header-top) 45%,var(--header-bottom) 100%)}
  .wordmark{position:absolute;left:0;top:140px;width:1200px;text-align:center;
    font-family:"Arimo",Arial,sans-serif;font-size:56px;letter-spacing:2px;color:var(--ink)}
  .wordmark-mark{display:inline-block;width:22px;height:22px;background:var(--brand-blue);
    margin-right:16px;vertical-align:middle;position:relative;top:-4px}

  .hero{position:absolute;left:0;top:232px;width:1200px;height:519px;background:var(--paper);
    box-shadow:0 -6px 10px rgba(0,0,0,.18),0 6px 10px rgba(0,0,0,.18)}
  .hero-visual{position:absolute;left:116px;top:20px;width:478px;height:420px;border-radius:12px;
    background:linear-gradient(135deg,#3a9fe0 0%,#1f7cc9 45%,#d9b566 75%,#f0d27e 100%)}
  .headline{position:absolute;left:627px;top:20px;font-family:"Marck Script",cursive;
    font-size:32.5px;line-height:40px;color:var(--brand-blue);white-space:nowrap}
  .categories{position:absolute;left:752px;top:164px;list-style:none;font-family:"Delius",cursive;
    font-size:24px;color:var(--ink)}
  .categories li{height:37px;display:flex;align-items:center}
  .categories svg{width:22px;height:22px;margin-right:6px}
  .join{position:absolute;left:752px;top:372px;width:303px;height:119px;border:1px solid #ccc;border-radius:8px;
    background:linear-gradient(180deg,#ffffff,#efefef);box-shadow:0 1px 3px rgba(0,0,0,.12)}
  .join-label{position:absolute;left:58px;top:4px;font-family:"Fredoka",sans-serif;font-weight:600;
    font-size:96px;line-height:110px;color:var(--join-yellow)}
  .join-badge{position:absolute;left:986px;top:332px;width:118px;height:118px}
  .join-badge span{position:absolute;left:0;top:28px;width:118px;text-align:center;font-family:"Marck Script",cursive;
    font-size:25px;line-height:26px;color:#fff}
  .tagline{position:absolute;left:26px;top:470px;font-family:"Marck Script",cursive;font-size:27px;color:var(--brand-blue);white-space:nowrap}

  .signup{position:absolute;left:26px;top:817px;font-family:"Marck Script",cursive;font-size:23px;color:var(--brand-blue)}
  .social{position:absolute;top:800px;width:64px;height:64px;border-radius:50%;background:var(--bar-blue);
    display:flex;align-items:center;justify-content:center;color:#fff;font-size:10px;font-family:"Arimo",Arial,sans-serif}
  .social.friendline{left:213px}
  .social.chirply{left:284px;background:var(--brand-blue)}

  .feed{position:absolute;top:780px;width:200px}
  .feed.news{left:500px}
  .feed.picks{left:853px}
  .feed h2{font-weight:400;font-size:20px;color:var(--ink);margin-left:2px;margin-bottom:17px}
  .feed ul{list-style:none}
  .feed li{position:relative;padding-left:23px;font-size:13px;line-height:17px;color:#333;margin-bottom:9px}
  .feed li::before{content:"";position:absolute;left:0;top:2px;width:14px;height:14px;border-radius:50%;
    background:radial-gradient(circle at 40% 35%,#9fd46b,#2f8ad0 60%,#1a5d9a)}
  .more{position:absolute;top:928px;width:65px;height:22px;border:1px solid #aaa;background:#fff;
    font-size:11px;line-height:20px;text-align:center;color:#333}
  .more.news{left:602px}
  .more.picks{left:955px}

  .site-footer{position:absolute;left:0;top:961px;width:1200px;height:42px;background:var(--bar-blue)}
  .copyright{position:absolute;right:22px;top:13px;font-size:13px;color:#fff}
</style>
</head>
<body>
<div class="page">
  <header class="site-header">
    <div class="wordmark"><span class="wordmark-mark"></span>tavernik</div>
  </header>

  <section class="hero">
    <div class="hero-visual" role="img" aria-label="Illustration of a globe with a golden magnifying glass"></div>
    <p class="headline">Discover your cities hottest offers<br>places &amp; venues while sharing<br>the things that mean the most to you</p>
    <ul class="categories">
      <li><svg viewBox="0 0 24 24"><polygon points="12,1 15,9 23,9 16.5,14 19,22 12,17 5,22 7.5,14 1,9 9,9" fill="#f5ad00"/></svg>Fashion &amp; Beauty</li>
      <li><svg viewBox="0 0 24 24"><polygon points="12,1 15,9 23,9 16.5,14 19,22 12,17 5,22 7.5,14 1,9 9,9" fill="#f5ad00"/></svg>Food &amp; Drinks</li>
      <li><svg viewBox="0 0 24 24"><polygon points="12,1 15,9 23,9 16.5,14 19,22 12,17 5,22 7.5,14 1,9 9,9" fill="#f5ad00"/></svg>Entertainment</li>
      <li><svg viewBox="0 0 24 24"><polygon points="12,1 15,9 23,9 16.5,14 19,22 12,17 5,22 7.5,14 1,9 9,9" fill="#f5ad00"/></svg>Events</li>
    </ul>
    <a class="join" href="#join"><span class="join-label">Join</span></a>
    <div class="join-badge">
      <svg viewBox="0 0 100 100" width="118" height="118"><polygon fill="#f5ad00" points="100,50 90.6,60.9 93.3,75 79.7,79.7 75,93.3 60.9,90.6 50,100 39.1,90.6 25,93.3 20.3,79.7 6.7,75 9.4,60.9 0,50 9.4,39.1 6.7,25 20.3,20.3 25,6.7 39.1,9.4 50,0 60.9,9.4 75,6.7 79.7,20.3 93.3,25 90.6,39.1"/></svg>
      <span>for free<br>Today!</span>
    </div>
    <p class="tagline">locate, explore and discover the best of your city with tavernik!!</p>
  </section>

  <p class="signup">You can Sign up :</p>
  <a class="social friendline" href="#friendline">Friendline</a>
  <a class="social chirply" href="#chirply">Chirply</a>

  <section class="feed news">
    <h2>Latest News</h2>
    <ul>
      <li>Lorem set magna sed diam sed diam.</li>
      <li>Lorem set magna sed diam sed diam.</li>
      <li>Lorem set magna sed diam sed diam.</li>
    </ul>
  </section>
  <a class="more news" href="#news">Lear more</a>

  <section class="feed picks">
    <h2>Top Picks</h2>
    <ul>
      <li>Lorem set magna sed diam sed diam.</li>
      <li>Lorem set magna sed diam sed diam.</li>
      <li>Lorem set magna sed diam sed diam.</li>
    </ul>
  </section>
  <a class="more picks" href="#picks">Lear more</a>

  <footer class="site-footer"><p class="copyright">Copyright@2011</p></footer>
</div>
</body>
</html>
```